Tallpine Company Flyer - RV Solar and Residential Solar

We would like to create a tri-fold brochure for our company for distribution in the mail. This will advertise our services, products and some references.

Our cover page should include a logo and contact information as well as some solar stock imagery.

Our inside pages should cover residential solar, RV solar and a solar education / facts portion.

The rear pages would be left for our remaining services and some references / testimonials.

Target Market(s)

Residential Homeowners and Recreational Vehicles

Industry/Entity Type

Solar Energy

Font styles to use
Serif
Sans Serif

Requirements
Must have
• Must match the color scheme of our logo.
Nice to have
• Solar stock images for RV solar and residential solar.
Either a black or white background with our logo is eye-catching,

```html
<!DOCTYPE html>
<html lang="en">
<head>
<meta charset="utf-8">
<title>Solar Brochure – Inside Spread</title>
<link href="https://fonts.googleapis.com/css2?family=Bree+Serif&family=Source+Sans+3:wght@300;400&display=swap" rel="stylesheet">
<style>
  :root {
    --backdrop: #e9ecef;
    --paper: #ffffff;
    --band: #4450a8;
    --heading-green: #8fc63f;
    --body-ink: #4b53a2;
    --tick: #6cb33f;
  }
  * { box-sizing: border-box; margin: 0; padding: 0; }
  html, body { width: 1200px; height: 800px; overflow: hidden; }
  body {
    background: var(--backdrop);
    font-family: "Source Sans 3", "Source Sans Pro", sans-serif;
    font-weight: 300;
    color: var(--body-ink);
  }
  .brochure {
    position: absolute;
    left: 110px; top: 20px;
    width: 980px; height: 760px;
    display: flex;
    background: var(--paper);
    box-shadow: 0 2px 10px rgba(0,0,0,.12);
  }
  .panel { position: relative; width: 33.333%; height: 100%; overflow: hidden; }
  .photo { position: absolute; left: 0; width: 100%; }
  .photo--house {
    top: 0; height: 248px;
    background: linear-gradient(170deg, #c9c3b6 0%, #8c8a7a 45%, #6f7a52 75%, #5b6b3c 100%);
  }
  .photo--plant {
    top: 248px; bottom: 0;
    background: linear-gradient(180deg, #2b3d8f 0%, #5b6aa8 30%, #9a9ea8 55%, #2a2d3a 75%, #5a4a3e 100%);
  }
  .photo--install {
    top: 0; height: 246px;
    background: linear-gradient(150deg, #6d8fd0 0%, #3052b4 40%, #1e3790 70%, #5c6a8a 100%);
  }
  .heading-band {
    position: absolute; left: 0;
    height: 42px;
    background: var(--band);
    display: flex; align-items: center; justify-content: center;
  }
  .heading-band h2 {
    font-family: "Bree Serif", serif;
    font-weight: 400;
    font-size: 22px;
    color: var(--heading-green);
    letter-spacing: .2px;
  }
  .heading-band--residential { top: 273px; width: 276px; }
  .heading-band--rv { top: 22px; width: 188px; }
  .heading-band--facts { top: 272px; width: 190px; }
  .feature-list {
    position: absolute; list-style: none;
    font-size: 15px; line-height: 1.05;
    hyphens: auto; -webkit-hyphens: auto;
  }
  .feature-list li { position: relative; padding-left: 24px; margin-bottom: 5px; }
  .feature-list svg { position: absolute; left: 0; top: 0; width: 15px; height: 15px; }
  .feature-list--residential { left: 20px; top: 340px; width: 280px; }
  .feature-list--rv { left: 22px; top: 84px; width: 262px; }
  .feature-list--rv li { margin-bottom: 6px; }
  .feature-list--facts { left: 23px; top: 341px; width: 292px; }
  .feature-list--facts li { margin-bottom: 5px; }
</style>
</head>
<body>
<svg width="0" height="0" style="position:absolute">
  <symbol id="tick" viewBox="0 0 16 16">
    <circle cx="8" cy="8" r="6.8" fill="none" stroke="var(--tick)" stroke-width="1.3"/>
    <path d="M4.8 8.2 L7.1 10.4 L11.3 5.8" fill="none" stroke="var(--tick)" stroke-width="1.4" stroke-linecap="round" stroke-linejoin="round"/>
  </symbol>
</svg>

<main class="brochure">
  <section class="panel panel--residential">
    <div class="photo photo--house" role="img" aria-label="Photo of a large white house with a driveway among trees at sunset"></div>
    <div class="heading-band heading-band--residential"><h2>Residential Rooftop PV</h2></div>
    <ul class="feature-list feature-list--residential">
      <li><svg><use href="#tick"/></svg>System sizes from 2.4kW to 12kW</li>
      <li><svg><use href="#tick"/></svg>DIY Packages available</li>
      <li><svg><use href="#tick"/></svg>Referral Bonus - 250$ for any successful solar referral</li>
      <li><svg><use href="#tick"/></svg>Offset some or all of your energy us</li>
      <li><svg><use href="#tick"/></svg>Electric Vehicle Charging System</li>
      <li><svg><use href="#tick"/></svg>Fully insured</li>
      <li><svg><use href="#tick"/></svg>25 Year system life</li>
      <li><svg><use href="#tick"/></svg>Can raise value of your home by up to $20,000</li>
      <li><svg><use href="#tick"/></svg>Extends the life of your roof</li>
      <li><svg><use href="#tick"/></svg>100$ donation to a local charity as part of any solar install.</li>
      <li><svg><use href="#tick"/></svg>One free solar panel if ordered within one week of your birthda</li>
      <li><svg><use href="#tick"/></svg>We offer financing.&nbsp; Finance a solar system with 20% down and you will be saving money immediately.&nbsp; Transfer the loan to your mortgage and increase your savings</li>
      <li><svg><use href="#tick"/></svg>Selling your house and love your solar?&nbsp; We will relocate the system to your new home for a small fee</li>
    </ul>
  </section>

  <section class="panel panel--rv">
    <div class="heading-band heading-band--rv"><h2>RV Solar</h2></div>
    <ul class="feature-list feature-list--rv">
      <li><svg><use href="#tick"/></svg>DIY 300W package from 500$.&nbsp; 600W package from 700</li>
      <li><svg><use href="#tick"/></svg>Installation services available</li>
      <li><svg><use href="#tick"/></svg>Keeps your batteries charged</li>
      <li><svg><use href="#tick"/></svg>No longer deal with dead batteries</li>
      <li><svg><use href="#tick"/></svg>Become the envy of all campers!</li>
      <li><svg><use href="#tick"/></svg>Never have a dead cell phone battery again</li>
    </ul>
    <div class="photo photo--plant" role="img" aria-label="Photo of solar panel arrays in front of cooling towers under a blue sky"></div>
  </section>

  <section class="panel panel--facts">
    <div class="photo photo--install" role="img" aria-label="Photo of a worker handling a blue solar panel"></div>
    <div class="heading-band heading-band--facts"><h2>Solar 101</h2></div>
    <ul class="feature-list feature-list--facts">
      <li><svg><use href="#tick"/></svg>Alberta is the sunniest province in Canada and comparable to Florida</li>
      <li><svg><use href="#tick"/></svg>Systems are designed to last 25 years but operate for as long as 40 year</li>
      <li><svg><use href="#tick"/></svg>Virtually no maintenance required</li>
      <li><svg><use href="#tick"/></svg>How your power bill works</li>
      <li><svg><use href="#tick"/></svg>Protect yourself from rising power costs</li>
      <li><svg><use href="#tick"/></svg>Not everyone can have solar.&nbsp; Once 30-40% of the market has solar, utilities will not allow all solar systems to be installed.</li>
      <li><svg><use href="#tick"/></svg>Dispel the snow myth:&nbsp; Snow only reduces a systems output by 5-8% over the course of a year.&nbsp; This is because our sunny hours are mostly made up in the longer summer days.</li>
      <li><svg><use href="#tick"/></svg>Solar panels are nearly indestructible. Hail cannot damage a solar panel</li>
      <li><svg><use href="#tick"/></svg>Any extra power generated in the summer is sold back to the grid as a</li>
    </ul>
  </section>
</main>
</body>
</html>
```